Visually Compelling Flyer Design - Harbor Perks

We are a life insurance company looking to create visually compelling flyers that gain attention of potential buyers and simplify the concept. It should be professional, friendly, approachable in nature. Our logo and several rough drafts are included.
We are looking to refine this look and make it ultra professional, clean and easy to follow. A creative brief with brand guidelines is also included.
FLYER 1 — PAY YOURSELF FIRST
EYEBROW TAG
YOUR COMPANY JUST UPGRADED YOUR BENEFITS
HEADLINE
One small decision. A lifetime of protection.
SUBHEADLINE
Permanent life insurance + long-term care coverage, starting at $1 a day.
EYEBROW TAG
CHOOSE YOUR DAILY INVESTMENT
STAT — TIER 1
$1 / day → $20,000 Life Insurance
STAT — TIER 2 (HERO — make this one biggest/most prominent)
$2 / day → $40,000 Life Insurance
★ Most Popular
STAT — TIER 3
$3 / day → $60,000 Life Insurance
CAPTION
Rate locked at enrollment. Benefit never decreases.
EYEBROW TAG
THREE BENEFITS. ONE POLICY.
SUBHEADLINE
Your money works three ways.
CALLOUT — BENEFIT 1
01 | Cash Value Growth
BODY
Averages 6% annually over the last 50 years — guaranteed never to fall below 3%. Better than any savings account. And if you ever need it, you can borrow against it. It's your money.
CALLOUT — BENEFIT 2
02 | Tax-Free Death Benefit
BODY
From day one, your family is protected. The full benefit is paid tax-free to the person you choose — no waiting period, no exceptions. That's your legacy, preserved.
CALLOUT — BENEFIT 3
03 | Long-Term Care Coverage
BODY
70% of Americans will need long-term care. This plan pays 75% of your benefit — upfront and tax-free — to cover those costs while you're still alive. Your retirement savings stay intact. Your family stays protected.
EYEBROW TAG
ALREADY HAVE LIFE INSURANCE THROUGH WORK?
SUBHEADLINE
That's term. It ends when you need it most.
BODY
Term life insurance is designed for temporary needs — protecting your paycheck, your mortgage, your kids while they're home. When you retire, the house is paid off and your children are grown. Term ends because the need ends.
BODY
But one need never ends: your final expenses and the cost of long-term care. This permanent plan stays with you after retirement — when term coverage is gone and getting new coverage is expensive or impossible.
COMPARISON — LEFT COLUMN HEADER
✕ TERM LIFE
COMPARISON — LEFT COLUMN ITEMS
Gets more expensive with age
Ends at retirement
No cash value
Temporary protection only
COMPARISON — RIGHT COLUMN HEADER
✓ THIS PLAN
COMPARISON — RIGHT COLUMN ITEMS
Rate locked forever at enrollment
Stays with you after retirement
Builds real cash value
Permanent protection for life
EYEBROW TAG
WHAT MAKES THIS DIFFERENT
SUBHEADLINE
Built for you. Stays with you.
CALLOUT
✓ Guaranteed Issued
No medical exams. No questions asked. You qualify.
CALLOUT
✓ Group Rate
Because you work here, you get pricing individuals can't access on their own.
CALLOUT
✓ Rate Locked Forever
Your premium never increases. Your benefit never decreases.
CALLOUT
✓ Portable
Change jobs. Retire. Your policy comes with you at the same rate.
CALLOUT
✓ Family Coverage
Protect your spouse and children under the same plan.
SUBHEADLINE
Protect retirement. Preserve dignity. Plan ahead.
CTA
Be on the lookout for your personalized coverage details.
CAPTION
Brokered by Harbor Perks · Underwritten by TrueLedger
FLYER 2 — THE LONG-TERM CARE REALITY
EYEBROW TAG
WHAT MOST PEOPLE DON'T KNOW — BUT SHOULD
HEADLINE
Most Americans are unprepared. You don't have to be.
SUBHEADLINE
The long-term care gap is real — and it affects families like yours.
EYEBROW TAG
THE NUMBERS ARE HARD TO IGNORE
STAT
70%
of Americans age 65 and older will need some form of long-term care during their lifetime.
CAPTION
Source: Pryce & Lomax, Review of Elder Welfare and Civic Planning, 2018
STAT
3–4%
of Americans over 50 own a private long-term care insurance policy. The gap between who needs it and who has it is staggering.
CAPTION
Source: Stroud & Bellamy, QVT Wellness Wire, 2023
STAT
$700 Billion+
Estimated annual U.S. long-term care cost — and it's growing every year.
CAPTION
Source: Delacroix Wynn & Pasternak, Civic Ledger Council, 2020
STAT
$470 Billion
The estimated value of unpaid care provided by family members every year. That's the real cost — measured in time, stress, and financial sacrifice.
CAPTION
Source: Tillman & Osei, Meridian Bureau
STAT
80%
of total long-term care spending goes directly to assist retirees. This isn't a young person's problem. But the time to plan is now.
CAPTION
SUBHEADLINE
Long-term care doesn't just cost money. It costs families.
BODY
When there's no plan in place, the people you love absorb the impact — financially, emotionally, and physically. Retirement savings built over a lifetime can disappear in months. Family members step back from their own lives to provide care. Dignity becomes a daily negotiation.
BODY
This is not inevitable. A small decision today changes the entire outcome.
EYEBROW TAG
THE SOLUTION
HEADLINE
The Pay Yourself First Principle.
BODY
Take the first $1, $2, or $3 you make every day and invest it in a permanent life insurance policy that includes long-term care coverage — underwritten by TrueLedger, offered through your employer at a group rate, and Guaranteed Issued for everyone.
STAT
$1 / day → $20,000 $2 / day → $40,000 $3 / day → $60,000
BODY
The benefit includes three protections in one: a cash value that grows at an average of 6% annually, a tax-free death benefit for your family, and long-term care coverage that pays 75% of your benefit upfront — tax-free — when you need care most.
SUBHEADLINE
Whether you're single, married, with children or without — there is protection in this plan for you.
HEADLINE
CTA
Look for your personalized offer. Coverage details are coming your way.
CAPTION
COPY RULES FOR DESIGNERS
Headlines are one idea only. Never more than two lines.
Stats stand alone. Never buried in a paragraph.
Body copy maxes at 3 sentences per block. If it's longer, cut it.
The $2/day tier is always the hero. Always.
"Guaranteed Issued" appears on both flyers. It's the most important trust signal.
TrueLedger is always attributed. Always.
The tagline is: Protect retirement. Preserve dignity. Plan ahead. — Use it verbatim.
Target Market(s)
Average Americans with a family - adults looking for life insurance
Industry/Entity Type
Life Insurance & Financial Retirement

```html
<!DOCTYPE html>
<html lang="en">
<head>
<meta charset="utf-8">
<title>Harbor Perks Flyers</title>
<link href="https://fonts.googleapis.com/css2?family=Montserrat:ital,wght@0,400;0,500;0,600;0,700;0,800;0,900;1,900&family=Roboto+Condensed:wght@600;700&family=Playfair+Display:ital@1&display=swap" rel="stylesheet">
<style>
:root{
  --board:#c8c8c8;
  --navy:#0c1766;
  --navy-mid:#15258f;
  --royal:#1c3aa8;
  --cyan:#6fe4f7;
  --cyan-bright:#3fd4f0;
  --ink:#111633;
  --body:#2a2f4a;
  --paper:#ffffff;
  --rule:#c9ccd8;
  --red:#e0342f;
}
*{box-sizing:border-box;margin:0;padding:0}
html,body{width:1200px;height:880px;overflow:hidden}
body{background:var(--board);font-family:"Montserrat",sans-serif;color:var(--ink);position:relative}
.flyer{position:absolute;top:94px;width:470px;height:609px;background:var(--paper);overflow:hidden;box-shadow:0 2px 6px rgba(0,0,0,.15)}
.flyer--one{left:83px}
.flyer--two{left:647px}
.abs{position:absolute}
.header-band{position:absolute;left:0;top:0;width:100%;height:162px;background:linear-gradient(180deg,var(--navy) 0%,var(--navy-mid) 100%)}
.headline{position:absolute;left:0;width:100%;text-align:center;font-weight:800;text-transform:uppercase;letter-spacing:.2px;line-height:1;white-space:nowrap}
.headline--white{color:#fff}
.headline--cyan{color:var(--cyan-bright)}
.subhead{position:absolute;left:0;width:100%;text-align:center;color:#fff;font-weight:500;line-height:1.2}
.subhead strong{color:var(--cyan);font-weight:700}

.tier{position:absolute;background:var(--cyan);border-radius:6px;text-align:center;color:var(--navy)}
.tier-badge{position:absolute;border-radius:50%;background:#fff;border:2px solid var(--navy);display:flex;align-items:center;justify-content:center;font-family:"Roboto Condensed",sans-serif;font-weight:700;color:var(--navy)}
.tier-badge small{font-family:"Montserrat",sans-serif;font-size:6px;font-weight:600;line-height:1;margin-left:1px;text-align:left}
.tier-amount{position:absolute;left:0;width:100%;font-family:"Roboto Condensed",sans-serif;font-weight:700;color:var(--royal);line-height:1}
.tier-amount sup{font-size:.5em;vertical-align:top;position:relative;top:.15em}
.tier-label{position:absolute;left:0;width:100%;font-size:11px;font-weight:500;color:var(--navy)}
.popular-tag{position:absolute;left:194px;top:229px;width:83px;height:12px;background:var(--navy);color:#fff;font-size:8px;font-weight:500;text-align:center;line-height:12px;white-space:nowrap}

.caption{font-size:8px;line-height:1.3;color:var(--ink)}
.pill{position:absolute;background:var(--navy-mid);color:#fff;font-weight:700;font-size:9px;border-radius:0 8px 8px 0;padding:0 8px;line-height:14px;letter-spacing:.3px;white-space:nowrap}
.section-head{position:absolute;color:var(--royal);font-weight:700;font-size:10px;line-height:1.05;text-transform:uppercase}
.lead{position:absolute;font-size:8px;font-weight:600;color:var(--ink);white-space:nowrap}
.body-copy{position:absolute;font-size:5.8px;line-height:1.35;color:var(--body)}
.body-copy b{color:var(--royal)}

.benefit-row{position:absolute;left:28px;width:226px;display:flex;align-items:center;gap:4px}
.benefit-chip{background:var(--navy-mid);color:#fff;font-size:4.5px;font-weight:800;border-radius:5px;padding:1px 3px}
.benefit-num{font-size:16px;font-weight:500;color:#a6a9b8;line-height:1}
.benefit-line{flex:1;height:1px;background:var(--rule)}
.benefit-title{position:absolute;left:28px;font-size:12px;font-weight:500;color:var(--ink)}

.compare{position:absolute;left:262px;top:372px;width:180px;height:86px;border-radius:4px;overflow:hidden;display:flex;border:1px solid var(--royal)}
.compare-col{width:50%;padding:6px 6px}
.compare-col--term{background:var(--cyan);color:var(--navy)}
.compare-col--plan{background:var(--navy-mid);color:#fff}
.compare-col h4{font-size:8px;font-weight:700;margin-bottom:3px}
.compare-col--plan h4{color:var(--cyan)}
.compare-col li{list-style:none;font-size:5.5px;line-height:1.3;margin-bottom:2px;padding-left:6px;position:relative}
.compare-col li::before{content:"";position:absolute;left:0;top:2px;width:3.5px;height:3.5px;border-radius:50%}
.compare-col--term li::before{background:var(--red)}
.compare-col--plan li::before{background:var(--cyan)}

.feature{position:absolute;width:110px}
.feature h5{font-size:6.5px;font-weight:600;color:var(--ink);padding-left:6px;position:relative}
.feature h5::before{content:"";position:absolute;left:0;top:2px;width:4px;height:4px;border-radius:50%;background:var(--royal)}
.feature p{font-size:5.5px;line-height:1.3;color:var(--body);padding-left:6px}

.brand{position:absolute;text-align:center;width:60px}
.brand-mark{width:40px;height:40px;border-radius:50%;border:3px solid var(--royal);margin:0 auto 4px}
.brand-name{font-size:11px;font-weight:600;color:var(--royal);line-height:1.05}
.taglines{position:absolute;display:flex;gap:10px;font-size:6.5px;font-weight:700;color:var(--royal);line-height:1}
.taglines span{display:inline-flex;align-items:center;gap:3px}
.taglines i{width:7px;height:7px;border-radius:50%;background:var(--cyan-bright);display:inline-block}
.script{position:absolute;font-family:"Playfair Display",serif;font-style:italic;font-size:8px;color:var(--royal);white-space:nowrap}
.cta-strong{position:absolute;font-size:6.5px;font-weight:600;color:var(--ink);white-space:nowrap}
.url-pill{position:absolute;background:var(--navy-mid);color:#fff;border-radius:0 9px 9px 0;font-size:10.5px;font-weight:600;padding-left:7px;box-shadow:2px 2px 0 var(--cyan);white-space:nowrap}

.stat-card{position:absolute;top:112px;width:98px;height:147px;background:var(--cyan);border-radius:5px;text-align:center;color:var(--navy)}
.stat-circle{position:absolute;left:50%;top:-25px;transform:translateX(-50%);width:48px;height:48px;border-radius:50%;background:#fff;border:2px solid var(--navy);display:flex;flex-direction:column;align-items:center;justify-content:center;font-weight:700;color:var(--royal);font-size:13px;line-height:1}
.stat-circle small{font-size:6px;font-weight:600}
.stat-text{position:absolute;left:5px;right:5px;top:34px;font-size:7px;line-height:1.3;font-weight:500}
.stat-source{position:absolute;left:5px;right:5px;top:98px;font-size:5.3px;line-height:1.3}
.stat-source b{display:block;font-weight:700}
.photo{position:absolute;border-radius:4px}
.closing{position:absolute;font-size:7.2px;font-weight:700;color:var(--ink);line-height:1.2}
.closing em{font-style:normal;color:var(--royal)}
.tier-row{position:absolute;left:246px;display:flex;align-items:center}
.tier-row-badge{width:46px;height:46px;border-radius:50%;border:2px solid var(--navy);background:#fff;display:flex;align-items:center;justify-content:center;font-family:"Roboto Condensed",sans-serif;font-weight:700;font-size:19px;color:var(--navy)}
.tier-row-badge small{font-family:"Montserrat",sans-serif;font-size:6px;font-weight:600;line-height:1;margin-left:1px}
.tier-row-value{margin-left:14px;font-family:"Roboto Condensed",sans-serif;font-weight:700;font-size:26px;color:var(--royal);line-height:1}
.tier-row-value sup{font-size:.5em;vertical-align:top}

.board-label{position:absolute;top:744px;font-weight:900;font-style:italic;font-size:44px;color:#000;letter-spacing:1px}
</style>
</head>
<body>

<section class="flyer flyer--one">
  <div class="header-band"></div>
  <h1 class="headline headline--white" style="top:22px;font-size:26px">One small decision.</h1>
  <h1 class="headline headline--cyan" style="top:47px;font-size:26px">A lifetime of protection.</h1>
  <p class="subhead" style="top:76px;font-size:12.5px">Permanent life insurance + long-term care coverage,<br>starting at <strong><sup>$</sup>1 a day.</strong></p>

  <div class="tier" style="left:86px;top:138px;width:91px;height:88px">
    <div class="tier-amount" style="top:52px;font-size:23px"><sup>$</sup>20,000</div>
    <div class="tier-label" style="top:72px">Life Insurance</div>
  </div>
  <div class="tier" style="left:182px;top:132px;width:106px;height:95px">
    <div class="tier-amount" style="top:55px;font-size:26px"><sup>$</sup>40,000</div>
    <div class="tier-label" style="top:79px">Life Insurance</div>
  </div>
  <div class="tier" style="left:294px;top:138px;width:90px;height:88px">
    <div class="tier-amount" style="top:52px;font-size:23px"><sup>$</sup>60,000</div>
    <div class="tier-label" style="top:72px">Life Insurance</div>
  </div>
  <div class="tier-badge" style="left:111px;top:120px;width:40px;height:40px;font-size:17px">$1<small>Per<br>Day</small></div>
  <div class="tier-badge" style="left:212px;top:110px;width:46px;height:46px;font-size:20px">$2<small>Per<br>Day</small></div>
  <div class="tier-badge" style="left:319px;top:120px;width:40px;height:40px;font-size:17px">$3<small>Per<br>Day</small></div>
  <svg class="abs" style="left:125px;top:158px" width="12" height="22" viewBox="0 0 12 22"><rect x="4" y="0" width="4" height="13" fill="#0c1766"/><path d="M0 12h12L6 22z" fill="#0c1766"/></svg>
  <svg class="abs" style="left:228px;top:154px" width="14" height="26" viewBox="0 0 14 26"><rect x="5" y="0" width="4" height="15" fill="#0c1766"/><path d="M0 14h14L7 26z" fill="#0c1766"/></svg>
  <svg class="abs" style="left:333px;top:158px" width="12" height="22" viewBox="0 0 12 22"><rect x="4" y="0" width="4" height="13" fill="#0c1766"/><path d="M0 12h12L6 22z" fill="#0c1766"/></svg>
  <div class="popular-tag">★ Most Popular ★</div>

  <p class="caption abs" style="left:28px;top:252px;width:160px">Rate locked at enrollment. Benefit never decreases.</p>
  <div class="pill" style="left:28px;top:274px;width:171px">THREE BENEFITS. ONE POLICY</div>
  <p class="lead" style="left:28px;top:291px">Your money works three ways.</p>

  <div class="benefit-row" style="top:305px"><span class="benefit-chip">BENEFIT</span><span class="benefit-num">01</span><span class="benefit-line"></span></div>
  <h3 class="benefit-title" style="top:323px">Cash Value Growth</h3>
  <p class="body-copy" style="left:28px;top:339px;width:204px">Averages <b>6%</b> annually over the last <b>50 years</b> — guaranteed never to fall below <b>3%</b>. Better than any savings account. And if you ever need it, you can borrow against it. It's your money.</p>

  <div class="benefit-row" style="top:366px"><span class="benefit-chip">BENEFIT</span><span class="benefit-num">02</span><span class="benefit-line"></span></div>
  <h3 class="benefit-title" style="top:384px">Tax-Free Death Benefit</h3>
  <p class="body-copy" style="left:28px;top:400px;width:204px">From day one, your family is protected. The full benefit is paid tax-free to the person you choose — no waiting period, no exceptions. That's your legacy, preserved.</p>

  <div class="benefit-row" style="top:428px"><span class="benefit-chip">BENEFIT</span><span class="benefit-num">03</span><span class="benefit-line"></span></div>
  <h3 class="benefit-title" style="top:447px">Long-Term Care Coverage</h3>
  <p class="body-copy" style="left:28px;top:463px;width:204px"><b>70%</b> of Americans will need long-term care. This plan pays <b>75%</b> of your benefit — upfront and tax-free — to cover those costs while you're still alive. Your retirement savings stay intact. Your family stays protected.</p>

  <h2 class="section-head" style="left:262px;top:253px;width:180px">Already have life insurance<br>through work?</h2>
  <p class="lead" style="left:262px;top:276px;font-size:7.5px">That's term. It ends when you need it most.</p>
  <p class="body-copy" style="left:262px;top:287px;width:175px">Term life insurance is designed for temporary needs — protecting your paycheck, your mortgage, your kids while they're home. When you retire, the house is paid off and your children are grown. Term ends because the need ends.</p>
  <p class="body-copy" style="left:262px;top:324px;width:175px">But one need never ends: your final expenses and the cost of long-term care. This permanent plan stays with you after retirement — when term coverage is gone and getting new coverage is expensive or impossible.</p>

  <div class="compare">
    <div class="compare-col compare-col--term">
      <h4>TERM LIFE</h4>
      <ul><li>Gets more expensive with age</li><li>Ends at retirement</li><li>No cash value</li></ul>
    </div>
    <div class="compare-col compare-col--plan">
      <h4>THIS PLAN</h4>
      <ul><li>Rate locked forever at enrollment</li><li>Stays with you after retirement</li><li>Builds real cash value</li><li>Permanent protection for life</li></ul>
    </div>
  </div>

  <h2 class="section-head" style="left:262px;top:473px">What makes this different</h2>
  <p class="lead" style="left:262px;top:484px;font-size:7.5px">Built for you. Stays with you.</p>
  <div class="feature" style="left:262px;top:498px"><h5>Guaranteed Issued</h5><p>No medical exams. No questions asked. You qualify.</p></div>
  <div class="feature" style="left:262px;top:525px"><h5>Rate Locked Forever</h5><p>Your premium never increases. Your benefit never decreases.</p></div>
  <div class="feature" style="left:262px;top:552px"><h5>Group Rate</h5><p>Because you work here, you get pricing individuals can't access on their own.</p></div>
  <div class="feature" style="left:376px;top:498px;width:84px"><h5>Portable</h5><p>Change jobs. Retire. Your policy comes with you at the same rate.</p></div>
  <div class="feature" style="left:376px;top:538px;width:84px"><h5>Family Coverage</h5><p>Protect your spouse and children under the same plan.</p></div>

  <div class="brand" style="left:25px;top:510px"><div class="brand-mark"></div><div class="brand-name">HARBOR<br>PERKS</div></div>
  <div class="taglines" style="left:89px;top:509px"><span><i></i>Protect<br>retirement.</span><span><i></i>Preserve<br>dignity.</span><span><i></i>Plan<br>ahead.</span></div>
  <p class="script" style="left:89px;top:526px">Be on the lookout for</p>
  <p class="cta-strong" style="left:89px;top:537px">your personalized coverage details.</p>
  <p class="caption abs" style="left:89px;top:547px;font-size:6.3px;width:160px">Brokered by Harbor Perks · Underwritten by TrueLedger</p>
  <div class="url-pill" style="left:89px;top:563px;width:145px;height:16px;line-height:16px">www.harborperks.com</div>
</section>

<section class="flyer flyer--two">
  <div class="header-band"></div>
  <h1 class="headline headline--white" style="top:22px;font-size:21px">Most Americans are unprepared.</h1>
  <h1 class="headline headline--cyan" style="top:43px;font-size:21px">You don't have to be.</h1>
  <p class="subhead" style="top:66px;font-size:12px">The long-term care gap is real – &amp; it affects families like yours.</p>

  <div class="stat-card" style="left:29px"><div class="stat-circle">70%</div>
    <p class="stat-text">Of Americans age 65 &amp; older will need some form of long-term care during their lifetime</p>
    <p class="stat-source"><b>Source</b>Pryce &amp; Lomax, Review of Elder Welfare and Civic Planning, 2018</p></div>
  <div class="stat-card" style="left:134px"><div class="stat-circle">3–4%</div>
    <p class="stat-text">Of Americans over 50 own a private long-term care insurance policy. The gap between who needs it &amp; who has it is staggering</p>
    <p class="stat-source" style="top:108px"><b>Source</b>Stroud &amp; Bellamy, QVT Wellness Wire, 2023</p></div>
  <div class="stat-card" style="left:239px"><div class="stat-circle"><span>$700</span><small>Billion+</small></div>
    <p class="stat-text">Estimated annual U.S. long-term care cost — and it's growing every year</p>
    <p class="stat-source" style="top:74px"><b>Source</b>Delacroix Wynn &amp; Pasternak, Civic Ledger Council, 2020</p></div>
  <div class="stat-card" style="left:344px"><div class="stat-circle">80%</div>
    <p class="stat-text">of total long-term care spending goes directly to assist retirees. This isn't a young person's problem. But the time to plan is now.</p>
    <p class="stat-source" style="top:88px"><b>Source</b>Tillman &amp; Osei, Meridian Bureau</p></div>

  <h2 class="section-head" style="left:29px;top:274px;width:200px">Long-term care doesn't just<br>cost money. It costs families.</h2>
  <p class="body-copy" style="left:29px;top:299px;width:194px">When there's no plan in place, the people you love absorb the impact — financially, emotionally, and physically. Retirement savings built over a lifetime can disappear in months. Family members step back from their own lives to provide care. Dignity becomes a daily negotiation.</p>
  <p class="body-copy" style="left:29px;top:345px;width:194px">This is not inevitable. A small decision today changes the entire outcome.</p>
  <div class="photo" role="img" aria-label="Photo of a grandfather sharing a happy moment with his granddaughter at home" style="left:29px;top:369px;width:94px;height:93px;background:linear-gradient(135deg,#b8825a,#e2c7a6 55%,#7f94b6)"></div>
  <div class="photo" role="img" aria-label="Photo of an older couple walking together along a sunny street" style="left:129px;top:369px;width:93px;height:93px;background:linear-gradient(135deg,#8a7a6c,#c9bfb2 50%,#5d6f8c)"></div>
  <p class="closing" style="left:29px;top:476px;width:210px">WHETHER YOU'RE SINGLE, MARRIED, WITH CHILDREN OR WITHOUT — <em>THERE IS PROTECTION IN THIS PLAN FOR YOU.</em></p>

  <div class="brand" style="left:25px;top:510px"><div class="brand-mark"></div><div class="brand-name">HARBOR<br>PERKS</div></div>
  <div class="taglines" style="left:90px;top:526px"><span><i></i>Protect<br>retirement.</span><span><i></i>Preserve<br>dignity.</span><span><i></i>Plan<br>ahead.</span></div>
  <p class="script" style="left:90px;top:543px">Look for your personalized offer</p>
  <p class="cta-strong" style="left:90px;top:553px">Coverage details are coming your way.</p>
  <p class="caption abs" style="left:90px;top:563px;font-size:6.3px;width:150px">Brokered by Harbor Perks · Underwritten by TrueLedger</p>

  <div class="pill" style="left:248px;top:272px;font-size:9px">THE SOLUTION</div>
  <p class="lead" style="left:248px;top:290px;font-size:7.5px">The Pay Yourself First Principle.</p>
  <p class="body-copy" style="left:248px;top:301px;width:196px">Take the first $1, $2, or $3 you make every day and invest it in a permanent life insurance policy that includes long-term care coverage — underwritten by TrueLedger, offered through your employer at a group rate, and Guaranteed Issued for everyone.</p>

  <div class="tier-row" style="top:347px"><div class="tier-row-badge">$1<small>Per<br>Day</small></div>
    <svg width="28" height="22" viewBox="0 0 28 22"><rect x="0" y="7" width="16" height="8" fill="#0c1766"/><path d="M14 0l14 11-14 11z" fill="#0c1766"/></svg>
    <span class="tier-row-value"><sup>$</sup>20,000</span></div>
  <div class="tier-row" style="top:408px"><div class="tier-row-badge">$2<small>Per<br>Day</small></div>
    <svg width="28" height="22" viewBox="0 0 28 22"><rect x="0" y="7" width="16" height="8" fill="#0c1766"/><path d="M14 0l14 11-14 11z" fill="#0c1766"/></svg>
    <span class="tier-row-value"><sup>$</sup>40,000</span></div>
  <div class="tier-row" style="top:467px"><div class="tier-row-badge">$3<small>Per<br>Day</small></div>
    <svg width="28" height="22" viewBox="0 0 28 22"><rect x="0" y="7" width="16" height="8" fill="#0c1766"/><path d="M14 0l14 11-14 11z" fill="#0c1766"/></svg>
    <span class="tier-row-value"><sup>$</sup>60,000</span></div>

  <p class="body-copy" style="left:248px;top:520px;width:196px">The benefit includes three protections in one: a cash value that grows at an average of 6% annually, a tax-free death benefit for your family, and long-term care coverage that pays 75% of your benefit upfront — tax-free — when you need care most.</p>
  <div class="url-pill" style="left:248px;top:562px;width:165px;height:18px;line-height:18px;font-size:11.5px">www.harborperks.com</div>
</section>

<div class="board-label" style="left:222px">FLYER 1</div>
<div class="board-label" style="left:782px">FLYER 2</div>

</body>
</html>
```